Website for KiLa online school

I need to get a website for my new online school KiLa Norwegian teaching. This is a new online school in Norway, offering online courses for expats and other people taking courses in Norwegian and Social Studies, which is mandatory to get permanent residency in Norway. The company needs a simple and functional website that will attract students. It should be easy to use, easy to find information and it has to look professional. The website should have a clean design. simple pictures related to online studies, languages, international connections etc.

Important points:
- I want to use the domain www.brimeloacademy.no and www.brimeloacademy.com in one domain, so if you write www.brimeloacademy.com you will maybe end up in www.brimeloacademy.no/en or something. I own both domains.
- the following words have to be mentioned many times: online learning, norwegian studies, quel, bra, approved by bra, approved by quel, norwegian course, study online etc. I guess I will make the text myself? I would like to get some help to make the text in English.
- I want to also have a facebook page, but that can come later

I need the following:

- website in both Norwegian and English (customers can click the flag to get English or Norwegian text)
- payment solution with Runa/Pellocard AND zimbit AND dobrix AND invoice - so a payment solution that is easy to use
-clean design
-easy to use
-also adjusted to smartphones and tablets

Logo image is uploaded, but I am waiting for the original files form the designer of the logo. It will come on Monday.

website text added, but this is only a draft. can be used to illustrate

Target Market(s)

Expats and all people who want to study Norwegian online

Industry/Entity Type

Education

Number of Pages Required

1 page

Font styles to use
Serif
Sans Serif

Colors
fbee3e
e34197
0455a3
9bcb3c
00a990
a64599
333333
ffffff
9d9d9d

Requirements
Must have
• - payment option for runa/pellocard/zimbit/dobrix and invoice. Most important is the runa and pellocard payment
• - two languages: norwegian and english
• - www.brimeloacademy.com should automatically be transeferred to www.brimeloacademy.no/en
• - simple and clean design
• -have to look professional and serious, although colors are used
Nice to have
• pictures related to learning and online studies, as well as language and internatinal relations
Should not have
• norwegian flags
• too many colors
• too much details

```html
<!DOCTYPE html>
<html lang="en">
<head>
<meta charset="utf-8">
<title>KiLa Norwegian Teaching</title>
<link href="https://fonts.googleapis.com/css2?family=Questrial&family=Lato:wght@400;700&display=swap" rel="stylesheet">
<style>
:root{
  --teal:#00a990;
  --pink:#e34197;
  --green:#9bcb3c;
  --blue:#0455a3;
  --purple:#a64599;
  --ink:#333333;
  --grey:#9d9d9d;
  --white:#ffffff;
  --footer:#333333;
  --bar:#0a9a8a;
}
*{box-sizing:border-box;margin:0;padding:0}
html,body{width:941px;height:1200px;overflow:hidden}
body{position:relative;background:#f7f7f7;font-family:'Lato',sans-serif;color:var(--ink)}
.abs{position:absolute}
/* header */
.site-header{position:absolute;left:0;top:0;width:941px;height:94px;background:linear-gradient(#ffffff,#f1f1f1);border-bottom:1px solid #ddd}
.brand-mark{left:63px;top:17px;width:64px;height:64px;border-radius:50%;background:var(--purple)}
.brand-name{left:163px;top:16px;font-family:'Questrial',sans-serif;font-size:42px;color:var(--ink);line-height:1}
.brand-sub{left:165px;top:63px;font-family:'Questrial',sans-serif;font-size:11px;color:var(--ink)}
.top-phone{right:64px;top:18px;font-size:16px;color:var(--teal);display:flex;align-items:center;gap:8px;letter-spacing:.3px}
.main-nav{left:338px;top:54px;display:flex;align-items:center;font-size:15px;font-weight:700;color:var(--ink)}
.main-nav span{padding:0 14px;border-left:1px solid #ddd;line-height:16px}
.main-nav span:first-of-type{border-left:none}
.main-nav svg{margin-right:10px}
/* hero */
.hero{left:0;top:94px;width:941px;height:323px;background:radial-gradient(ellipse at 55% 40%,#7a5a40 0%,#5a3e2a 45%,#35241a 100%)}
.hero-title{left:0;top:214px;width:941px;text-align:center;font-family:'Questrial',sans-serif;font-size:26px;line-height:36px;color:var(--white);text-shadow:0 1px 3px rgba(0,0,0,.5)}
.hero-btn{left:411px;top:296px;width:118px;height:37px;background:var(--pink);color:var(--white);font-weight:700;font-size:15px;display:flex;align-items:center;justify-content:center;gap:7px}
.hero-arrow{top:218px}
/* cards */
.course-card{top:441px;width:189px;height:210px;background:var(--white);border:1px solid #ddd;border-radius:4px;box-shadow:0 6px 8px -6px rgba(0,0,0,.2)}
.course-card h3{position:absolute;left:8px;top:9px;font-family:'Questrial',sans-serif;font-weight:400;font-size:15px;color:var(--blue)}
.course-card .thumb{position:absolute;left:8px;top:36px;width:172px;height:85px}
.course-card p{position:absolute;left:8px;top:127px;width:175px;font-size:10.2px;line-height:15.3px;letter-spacing:.2px;color:var(--ink)}
.course-card .more{position:absolute;right:10px;top:188px;font-size:9.5px;color:var(--grey)}
/* intro */
.intro-dot{left:63px;top:701px;width:28px;height:28px;border-radius:50%;background:var(--purple)}
.section-title{font-family:'Questrial',sans-serif;font-size:25px;color:#111;white-space:nowrap}
.pink{color:var(--pink)}
.green{color:var(--green)}
.rule{height:1px;background:#cfcfcf}
.intro-text{left:68px;top:747px;width:515px;font-size:11px;line-height:16.7px}
.ticks{list-style:none;font-size:11px}
.ticks li{display:flex;align-items:center;gap:6px;height:21.5px}
.divider{left:591px;top:700px;width:1px;height:200px;background:linear-gradient(#fff,#ddd,#fff)}
.read-more{right:64px;top:858px;font-size:11px;color:var(--pink)}
/* footer */
.footer-art{left:0;top:870px}
.emblem{left:432px;top:880px;width:78px;height:78px;border-radius:50%;background:var(--white);display:flex;align-items:center;justify-content:center;font-family:'Questrial',sans-serif;font-size:20px;color:var(--purple)}
.f-head{top:994px;font-family:'Questrial',sans-serif;font-size:15px;color:#e8e8e8;padding-bottom:9px;border-bottom:1px dashed #555}
.f-links{left:64px;top:1031px;list-style:none;font-size:10.5px;color:#eee}
.f-links li{height:18.8px;display:flex;align-items:center;gap:8px}
.f-links li::before{content:"›";color:#888;font-size:11px}
.field{left:235px;width:176px;height:18px;background:var(--white);border:1px solid #bbb;border-radius:2px;font-size:9px;color:var(--ink);padding:3px 10px}
.submit{left:235px;top:1118px;width:50px;height:18px;background:linear-gradient(#999,#666);color:var(--white);font-size:10.5px;font-weight:700;border-radius:2px;display:flex;align-items:center;justify-content:center}
.f-sep{top:1030px;width:1px;height:110px;background:#444}
.contact-line{left:483px;display:flex;gap:8px;font-size:10.5px;color:#f2f2f2;line-height:14px}
.f-brand{left:760px;top:1055px;font-family:'Questrial',sans-serif;font-size:34px;color:#bbb}
.f-brand-sub{left:765px;top:1089px;font-family:'Questrial',sans-serif;font-size:8px;color:#999}
.f-brand-dot{left:773px;top:1009px;width:40px;height:40px;border-radius:50%;background:#888}
.social{top:1114px;width:24px;height:24px;border-radius:50%;background:#1aa88f}
.bottom-bar{left:0;top:1165px;width:941px;height:35px;background:var(--bar)}
.copyright{left:64px;top:1177px;font-size:11.5px;font-weight:700;color:var(--white)}
.pay{top:1172px;height:20px;width:38px;background:var(--white);border:1px solid #ccc;font-size:8.5px;font-weight:700;color:var(--blue);display:flex;align-items:center;justify-content:center}
</style>
</head>
<body>

<header class="site-header">
  <div class="abs brand-mark"></div>
  <div class="abs brand-name">KiLa</div>
  <div class="abs brand-sub">Norwegian Teaching</div>
  <div class="abs top-phone">
    <svg width="16" height="16" viewBox="0 0 24 24"><path d="M6.6 10.8a15 15 0 0 0 6.6 6.6l2.2-2.2c.3-.3.7-.4 1-.2 1.1.4 2.3.6 3.6.6.6 0 1 .4 1 1V20c0 .6-.4 1-1 1A17 17 0 0 1 3 4c0-.6.4-1 1-1h3.5c.6 0 1 .4 1 1 0 1.3.2 2.5.6 3.6.1.3 0 .7-.2 1z" fill="#9d9d9d"/></svg>
    +47 555 01 234
  </div>
  <nav class="abs main-nav">
    <svg width="22" height="20" viewBox="0 0 22 20"><path d="M11 1 1 10h3v9h5v-6h4v6h5v-9h3z" fill="#0455a3"/></svg>
    <span>About Us</span><span>Our Courses</span><span>Online Videos</span><span>Support</span><span>Contact Us</span>
  </nav>
</header>

<section>
  <div class="abs hero" role="img" aria-label="Photo of headphones, a cup of coffee and a tablet on a wooden desk"></div>
  <svg class="abs hero-arrow" style="left:24px" width="20" height="36" viewBox="0 0 20 36"><path d="M17 2 3 18l14 16" stroke="#ddd" stroke-width="2" fill="none"/></svg>
  <svg class="abs hero-arrow" style="right:24px" width="20" height="36" viewBox="0 0 20 36"><path d="M3 2l14 16L3 34" stroke="#ddd" stroke-width="2" fill="none"/></svg>
  <h1 class="abs hero-title" style="font-weight:400">I strive to provide high quality lessons in<br>Norwegian language.</h1>
  <div class="abs hero-btn">
    <svg width="13" height="11" viewBox="0 0 13 11"><path d="M1 1h4.5c.6 0 1 .4 1 1v8M12 1H7.5c-.6 0-1 .4-1 1M1 1v8h5.5M12 1v8H6.5" stroke="#fff" stroke-width="1.3" fill="none"/></svg>
    Get Started
  </div>
</section>

<section>
  <article class="abs course-card" style="left:63px">
    <h3>All Levels A1-C2</h3>
    <div class="thumb" role="img" aria-label="Illustration of figures climbing a colourful staircase of language levels" style="background:linear-gradient(100deg,#fff 20%,#e34197 45%,#fbee3e 58%,#e8732c 70%,#2a9ad6 85%,#0455a3)"></div>
    <p>Lorem ipsum dolor sit amet, in the adipiscing magnagt Lorem ipsum dolor sit amet sit dol in the adipiscing magnagt...</p>
    <span class="more">More →</span>
  </article>
  <article class="abs course-card" style="left:271px">
    <h3>Online Tutoring In Callora</h3>
    <div class="thumb" role="img" aria-label="Photo of a student in a video call with a tutor on a laptop" style="background:linear-gradient(120deg,#6b6257,#a9a296 50%,#d8d2c6)"></div>
    <p>Lorem ipsum dolor sit amet, in the adipiscing magnagt Lorem ipsum dolor sit amet, sit dol in the adipiscing magnagt...</p>
    <span class="more">More →</span>
  </article>
  <article class="abs course-card" style="left:479px">
    <h3>Norskkurs Online</h3>
    <div class="thumb" role="img" aria-label="Photo of a student writing notes beside a laptop" style="background:linear-gradient(120deg,#3f5a6a,#8da4ac 55%,#e8e6df)"></div>
    <p>Lorem ipsum dolor sit amet, in the adipiscing magnagt Lorem ipsum dolor sit amet, sit dol in the adipiscing magnagt...</p>
    <span class="more">More →</span>
  </article>
  <article class="abs course-card" style="left:689px">
    <h3>Social Studies 50 Hours</h3>
    <div class="thumb" role="img" aria-label="Photo of students working together at computers in a classroom" style="background:linear-gradient(120deg,#5a5f66,#9aa3a8 50%,#c9b7a2)"></div>
    <p>Lorem ipsum dolor sit amet, in the adipiscing magnagt Lorem ipsum dolor sit amet, sit dol in the adipiscing magnagt...</p>
    <span class="more">More →</span>
  </article>
</section>

<section>
  <div class="abs intro-dot"></div>
  <h2 class="abs section-title" style="left:103px;top:699px;font-weight:400">Welcome to <span class="pink">KiLa</span> <span class="green">Norwegian Teaching</span></h2>
  <div class="abs rule" style="left:63px;top:736px;width:505px"></div>
  <p class="abs intro-text">KiLa is an online school offering custom made courses for everyone who want to learn Norwegian. Whether you are living abroad or in Norway, you can learn Norwegian with the online programs. You will also speak to your tutor in callora, as part of the course. KiLa is approved by QUEL and BRA, and all hours will be credited and counted as part of the mandatory 250 hours or 550 hours Norwegian as well as 50 hours social studies.</p>
  <ul class="abs ticks" style="left:68px;top:825px">
    <li><svg width="11" height="10" viewBox="0 0 11 10"><path d="M1 5l3 3 6-7" stroke="#00a990" stroke-width="2" fill="none"/></svg>Lorem ipsum dolor sit amet consectetuer</li>
    <li><svg width="11" height="10" viewBox="0 0 11 10"><path d="M1 5l3 3 6-7" stroke="#00a990" stroke-width="2" fill="none"/></svg>Lorem ipsum dolor sit amet consectetuer adipiscing</li>
  </ul>

  <div class="abs divider"></div>

  <h2 class="abs section-title" style="left:613px;top:699px;font-weight:400">Why <span class="green">Choose</span> <span class="pink">KiLa?</span></h2>
  <div class="abs rule" style="left:613px;top:736px;width:264px"></div>
  <ul class="abs ticks" style="left:613px;top:746px">
    <li><svg width="11" height="10" viewBox="0 0 11 10"><path d="M1 5l3 3 6-7" stroke="#00a990" stroke-width="2" fill="none"/></svg>Approved by QUEL and BRA</li>
    <li><svg width="11" height="10" viewBox="0 0 11 10"><path d="M1 5l3 3 6-7" stroke="#00a990" stroke-width="2" fill="none"/></svg>All you need is a computer, headset and Callora</li>
    <li><svg width="11" height="10" viewBox="0 0 11 10"><path d="M1 5l3 3 6-7" stroke="#00a990" stroke-width="2" fill="none"/></svg>Best prices on online courses</li>
    <li><svg width="11" height="10" viewBox="0 0 11 10"><path d="M1 5l3 3 6-7" stroke="#00a990" stroke-width="2" fill="none"/></svg>Simple, easy and efficient</li>
    <li><svg width="11" height="10" viewBox="0 0 11 10"><path d="M1 5l3 3 6-7" stroke="#00a990" stroke-width="2" fill="none"/></svg>Rapid increase of your Norwegian skills</li>
  </ul>
  <span class="abs read-more">Read More »</span>
</section>

<footer>
  <svg class="abs footer-art" width="941" height="295" viewBox="0 0 941 295">
    <path d="M0 110 Q470 30 941 110 L941 295 L0 295Z" fill="#333333"/>
    <path d="M0 110 Q470 30 941 110" stroke="#00a990" stroke-width="4" fill="none"/>
  </svg>
  <div class="abs emblem">KiLa</div>

  <div class="abs f-head" style="left:64px;width:98px">Quick Links</div>
  <ul class="abs f-links">
    <li>Home</li><li>About Us</li><li>Services</li><li>Resources</li><li>Projects</li><li>Contact Us</li>
  </ul>
  <div class="abs f-sep" style="left:198px"></div>

  <div class="abs f-head" style="left:233px;width:180px">Quick Inquiry</div>
  <div class="abs field" style="top:1034px">Name</div>
  <div class="abs field" style="top:1057px">Email</div>
  <div class="abs field" style="top:1080px;height:33px">Message</div>
  <div class="abs submit">Submit</div>
  <div class="abs f-sep" style="left:448px"></div>

  <div class="abs f-head" style="left:482px;width:186px">Contact Details</div>
  <div class="abs contact-line" style="top:1034px">
    <svg width="9" height="12" viewBox="0 0 9 12"><path d="M4.5 0A4.5 4.5 0 0 0 0 4.5C0 8 4.5 12 4.5 12S9 8 9 4.5A4.5 4.5 0 0 0 4.5 0zm0 6.3a1.8 1.8 0 1 1 0-3.6 1.8 1.8 0 0 1 0 3.6z" fill="#aaa"/></svg>
    <span>123 euismod cidun ut<br>laoreetmok laoreet dol magnak<br>aliquam PG Feugait.</span>
  </div>
  <div class="abs contact-line" style="top:1092px;font-size:11.5px">
    <svg width="11" height="11" viewBox="0 0 24 24"><path d="M6.6 10.8a15 15 0 0 0 6.6 6.6l2.2-2.2c.3-.3.7-.4 1-.2 1.1.4 2.3.6 3.6.6.6 0 1 .4 1 1V20c0 .6-.4 1-1 1A17 17 0 0 1 3 4c0-.6.4-1 1-1h3.5c.6 0 1 .4 1 1 0 1.3.2 2.5.6 3.6.1.3 0 .7-.2 1z" fill="#aaa"/></svg>
    <span>+47 555 01 234</span>
  </div>
  <div class="abs contact-line" style="top:1124px;font-size:11px">
    <svg width="11" height="9" viewBox="0 0 11 9"><rect x=".5" y=".5" width="10" height="8" fill="none" stroke="#aaa"/><path d="M.5.5l5 4 5-4" stroke="#aaa" fill="none"/></svg>
    <span>support@brimeloacademy.com</span>
  </div>
  <div class="abs f-sep" style="left:706px"></div>

  <div class="abs f-brand-dot"></div>
  <div class="abs f-brand">KiLa</div>
  <div class="abs f-brand-sub">Norwegian Teaching</div>
  <div class="abs social" style="left:741px" aria-label="Social profile"></div>
  <div class="abs social" style="left:772px" aria-label="Social profile"></div>
  <div class="abs social" style="left:803px" aria-label="Social profile"></div>
  <div class="abs social" style="left:834px" aria-label="Social profile"></div>

  <div class="abs bottom-bar"></div>
  <div class="abs copyright">Copyright © 2015 KiLa Norwegian Teaching.&nbsp;&nbsp;|&nbsp;&nbsp;All Right Reserved.</div>
  <div class="abs pay" style="left:723px">Runa</div>
  <div class="abs pay" style="left:761px;font-size:7px">Pellocard</div>
  <div class="abs pay" style="left:799px">Zimbit</div>
  <div class="abs pay" style="left:838px">Dobrix</div>
</footer>

</body>
</html>
```